Accountability Project Graphics

I want to create 10 social media graphics (new Instagram size 4:5 (1080 x 1350 pixels) focusing on our Kelmora Accountability App, using any of the 3 pictures attached. Use the attached pics only, NO RANDOM STOCK PHOTOGRAPHY. For the color scheme, use the landing page colors/fonts (attached).
You can add any of the 3 photos attached but I mainly need BOLD text that includes these headlines and sub-headlines on them.
Please NOTE for all the headlines below, also add this sub-headline on each graphic:
Stay Consistent with MB in Your Pocket!
Here are the headlines:
• Stop Starting Over Every Monday
• You don't need more willpower. You need more support
• Built for women who are tired of doing this alone
• When Motivation Fades, MB Checks In
• The Support System You've Been Missing
• Support When Motivation Disappears
• What if MB Checked in Every Day?
• The Missing Piece Isn't Another Diet
• Eat the food you love. Stay accountable every day.
• One Bad Meal Doesn't Mean You Failed
women over 40 trying to lose weight

```html
<!DOCTYPE html>
<html lang="en">
<head>
<meta charset="utf-8">
<title>Kelmora Accountability App – Social Graphics</title>
<link rel="stylesheet" href="https://fonts.googleapis.com/css2?family=Playfair+Display:wght@700&family=Domine:wght@500&family=Poppins:ital,wght@1,600&display=swap">
<style>
:root{
  --page:#e6e6e6;
  --plum:#2f1f45;
  --rose:#c85a7c;
  --blush:#fdeef3;
  --lavender:#eadcf7;
  --white:#ffffff;
  --photo-warm-a:#d9c3ad;
  --photo-warm-b:#4a3a3f;
}
*{margin:0;padding:0;box-sizing:border-box}
html,body{width:1200px;height:2785px;overflow:hidden;background:var(--page)}
.board{position:relative;width:1200px;height:2785px}
.post{position:absolute;width:371px;height:463px;overflow:hidden;background:var(--blush)}
.col-a{left:222px}.col-b{left:608px}
.row-1{top:197px}.row-2{top:679px}.row-3{top:1161px}.row-4{top:1643px}.row-5{top:2125px}
.photo{position:absolute;left:0;top:0;width:100%}
.photo--solo{background:linear-gradient(160deg,#8a7c74 0%,#3b3540 45%,#1c1a26 70%,#9b2a3c 100%)}
.photo--duo{background:linear-gradient(170deg,#eee2d3 0%,#d6c2ae 40%,#3e4c6e 65%,#2a3550 100%)}
.photo--hug{background:linear-gradient(150deg,#e3c6e6 0%,#3a2630 40%,#e64f86 65%,#d8f5a6 100%)}
.tagline{position:absolute;left:0;bottom:0;width:100%;height:46px;display:flex;align-items:center;justify-content:center;
  font-family:"Poppins",sans-serif;font-style:italic;font-weight:600;font-size:14px;color:var(--white);letter-spacing:.3px}
.tagline--plum{background:var(--plum)}
.tagline--rose{background:var(--rose)}
.headline{position:absolute;font-family:"Domine",serif;font-weight:500;line-height:1.12;letter-spacing:1px}
.headline--bold{font-family:"Playfair Display",serif;font-weight:700;letter-spacing:0}
.band{position:absolute;left:0;width:100%;display:flex;flex-direction:column;align-items:center;justify-content:center;text-align:center;color:var(--white)}
</style>
</head>
<body>
<main class="board">

  <!-- 1 -->
  <section class="post col-a row-1">
    <div class="photo photo--solo" style="height:417px" role="img" aria-label="Coach in a black lace outfit smiling beside a red pool table"></div>
    <h2 class="headline headline--bold" style="left:227px;top:22px;font-size:37px;line-height:41px;color:var(--white)">Stop<br>Starting<br>Over<br>Every<br>Monday</h2>
    <p class="tagline tagline--plum">Stay Consistent with MB in Your Pocket!</p>
  </section>

  <!-- 2 -->
  <section class="post col-b row-1">
    <div class="photo photo--duo" style="height:417px" role="img" aria-label="Coach and client in denim laughing together in a bright room"></div>
    <h2 class="headline" style="right:18px;top:36px;font-size:28px;line-height:34px;text-align:right;color:var(--plum)">You Don't Need<br>More Willpower.<br>You Need<br>More<br>Support</h2>
    <p class="tagline tagline--rose">Stay Consistent with MB in Your Pocket!</p>
  </section>

  <!-- 3 -->
  <section class="post col-a row-2" style="background:linear-gradient(180deg,#e2b9d2,#d6b4e6)">
    <div class="photo photo--hug" style="left:140px;top:70px;width:231px;height:347px" role="img" aria-label="Coach in pink hugging a smiling client"></div>
    <h2 class="headline headline--bold" style="left:25px;top:14px;font-size:36px;line-height:43px;color:var(--plum)">Built For<br>Women<br>Who<br>Are<br>Tired<br>Of<br>Doing<br>This<br>Alone</h2>
    <p class="tagline tagline--rose">Stay Consistent with MB in Your Pocket!</p>
  </section>

  <!-- 4 -->
  <section class="post col-b row-2" style="background:var(--lavender)">
    <div class="band" style="top:0;height:103px;background:var(--plum)">
      <h2 class="headline" style="position:static;font-size:28px;line-height:36px">When Motivation<br>Fades, MB Checks In</h2>
    </div>
    <svg width="371" height="314" style="position:absolute;top:103px;left:0" role="img" aria-label="Coach and client in denim laughing together">
      <defs><linearGradient id="duo4" x1="0" y1="0" x2="0" y2="1"><stop offset="0" stop-color="#eee2d3"/><stop offset=".45" stop-color="#d2bca8"/><stop offset=".7" stop-color="#3e4c6e"/><stop offset="1" stop-color="#2a3550"/></linearGradient></defs>
      <polygon points="0,0 280,0 371,314 75,314 0,60" fill="url(#duo4)"/>
    </svg>
    <p class="tagline tagline--rose">Stay Consistent with MB in Your Pocket!</p>
  </section>

  <!-- 5 -->
  <section class="post col-a row-3">
    <div class="photo photo--hug" style="top:197px;height:266px" role="img" aria-label="Coach in pink hugging a smiling client"></div>
    <div class="band" style="top:0;height:197px;background:var(--plum)">
      <h2 class="headline" style="position:static;font-size:40px;line-height:42px">The Support<br>System You've<br>Been Missing</h2>
      <p style="margin-top:8px;padding-top:6px;border-top:1px solid var(--rose);width:280px;font-family:'Poppins',sans-serif;font-style:italic;font-weight:600;font-size:13px">Stay Consistent with MB in Your Pocket!</p>
    </div>
  </section>

  <!-- 6 -->
  <section class="post col-b row-3" style="background:var(--blush)">
    <div class="photo photo--solo" style="left:15px;top:26px;width:340px;height:284px;border-radius:170px 170px 0 0" role="img" aria-label="Coach in a black lace outfit smiling beside a red pool table"></div>
    <div class="band" style="left:15px;width:340px;top:310px;height:107px;background:var(--rose);opacity:.92">
      <h2 class="headline" style="position:static;font-size:26px;line-height:30px">Support When<br>Motivation Disappears</h2>
    </div>
    <p class="tagline tagline--plum">Stay Consistent with MB in Your Pocket!</p>
  </section>

  <!-- 7 -->
  <section class="post col-a row-4">
    <div class="photo photo--duo" style="height:336px" role="img" aria-label="Coach and client in denim laughing together"></div>
    <div class="band" style="top:336px;height:81px;background:var(--plum)">
      <h2 class="headline" style="position:static;font-size:26px;line-height:30px">What If MB Checked<br>In Every Day?</h2>
    </div>
    <p class="tagline tagline--plum">Stay Consistent with MB in Your Pocket!</p>
  </section>

  <!-- 8 -->
  <section class="post col-b row-4" style="background:var(--rose)">
    <div class="photo photo--solo" style="top:90px;height:327px;-webkit-mask-image:linear-gradient(180deg,transparent 0,#000 30%);mask-image:linear-gradient(180deg,transparent 0,#000 30%)" role="img" aria-label="Coach in a black lace outfit smiling beside a red pool table"></div>
    <h2 class="headline" style="left:0;width:100%;top:14px;text-align:center;font-size:26px;line-height:30px;color:var(--white)">The Missing Piece<br>Isn't Another Diet</h2>
    <p class="tagline tagline--plum">Stay Consistent with MB in Your Pocket!</p>
  </section>

  <!-- 9 -->
  <section class="post col-a row-5">
    <div class="photo photo--duo" style="height:322px" role="img" aria-label="Coach and client in denim laughing together"></div>
    <div class="band" style="top:322px;height:95px;background:var(--rose)">
      <h2 class="headline" style="position:static;font-size:26px;line-height:30px">One Bad Meal<br>Doesn’t Mean You Failed</h2>
    </div>
    <p class="tagline tagline--plum">Stay Consistent with MB in Your Pocket!</p>
  </section>

  <!-- 10 -->
  <section class="post col-b row-5" style="background:var(--rose)">
    <div class="photo photo--hug" style="height:292px" role="img" aria-label="Coach in pink hugging a smiling client"></div>
    <div class="band" style="top:292px;height:125px">
      <h2 class="headline" style="position:static;font-size:26px;line-height:30px">Eat the food you love.<br>Stay accountable<br>every day.</h2>
    </div>
    <p class="tagline tagline--rose">Stay Consistent with MB in Your Pocket!</p>
  </section>

</main>
</body>
</html>
```